Bref créative
Business cards and letterhead for a veterinary hospital
Marlow Ridge Veterinary Hospital
Professional
Glen H. Barrett, DVM, DABVP
Board certified, Canine and Feline Practice
5720 FM 916
Alder Bend, TX 75190
mrvhvet@fenmail.example
www.marlowridgevet.example

```html
<!DOCTYPE html>
<html lang="en">
<head>
<meta charset="utf-8">
<title>Marlow Ridge Veterinary Hospital — Business Card</title>
<link rel="stylesheet" href="https://fonts.googleapis.com/css2?family=Cinzel:wght@400;600&display=swap">
<style>
  :root {
    --page: #d9dadc;
    --tan: #c89a7c;
    --tan-light: #d6ad90;
    --navy: #1f3a7c;
    --ink: #ffffff;
    --card-w: 560px;
    --card-h: 320px;
  }
  * { margin: 0; padding: 0; box-sizing: border-box; }
  html, body { width: 1200px; height: 895px; overflow: hidden; }
  body {
    background: var(--page);
    font-family: "Cinzel", "Times New Roman", serif;
    position: relative;
  }
  .card {
    position: absolute;
    width: var(--card-w);
    height: var(--card-h);
    overflow: hidden;
    background: var(--tan);
    box-shadow: 0 2px 6px rgba(0,0,0,0.12);
  }
  .card--back { left: 560px; top: 110px; }
  .card--front { left: 100px; top: 470px; }

  .brand-dot {
    width: 26px; height: 26px; border-radius: 50%;
    background: var(--navy);
    flex: none;
  }
  .brand-name {
    color: var(--navy);
    font-weight: 600;
    text-transform: uppercase;
    text-align: center;
    line-height: 1.15;
  }

  /* Back face */
  .back-row {
    position: absolute;
    left: 0; right: 0; top: 130px;
    display: flex; align-items: center; justify-content: center; gap: 22px;
  }
  .back-url {
    color: var(--navy);
    font-size: 12px;
    letter-spacing: 3px;
    text-transform: uppercase;
  }
  .back-brand {
    display: flex; flex-direction: column; align-items: center; gap: 6px;
  }
  .back-brand .brand-name { font-size: 11px; letter-spacing: 1.5px; }
  .back-brand .brand-name small { display: block; font-size: 7px; letter-spacing: 1.5px; }

  /* Front face */
  .front-wave { position: absolute; inset: 0; }
  .front-brand {
    position: absolute;
    left: 0; right: 0; top: 42px;
    display: flex; flex-direction: column; align-items: center; gap: 6px;
  }
  .front-brand .brand-name { font-size: 19px; letter-spacing: 2px; }
  .front-brand .brand-name small { display: block; font-size: 11px; letter-spacing: 2.5px; }
  .details {
    position: absolute;
    left: 36px; right: 30px; top: 196px;
    color: var(--ink);
  }
  .holder-name { font-size: 16px; letter-spacing: 1px; }
  .holder-title { font-size: 8px; letter-spacing: 1px; text-transform: uppercase; margin-top: 3px; opacity: 0.9; }
  .detail-cols { display: flex; margin-top: 12px; }
  .address {
    font-style: normal;
    font-size: 10px; letter-spacing: 1px; line-height: 1.7; text-transform: uppercase;
    padding-right: 12px; border-right: 1px solid var(--tan-light);
  }
  .contacts { list-style: none; padding-left: 12px; font-size: 10px; letter-spacing: 0.6px; line-height: 1.7; text-transform: uppercase; }
  .contacts li { display: flex; align-items: center; gap: 6px; }
  .contacts svg { width: 10px; height: 10px; flex: none; }
  .contacts .email { text-transform: none; }
</style>
</head>
<body>

  <section class="card card--back" aria-label="Business card, back">
    <div class="back-row">
      <p class="back-url">www.marlowridgevet.example</p>
      <div class="back-brand">
        <span class="brand-dot"></span>
        <span class="brand-name">Marlow Ridge<small>Veterinary Hospital</small></span>
      </div>
    </div>
  </section>

  <section class="card card--front" aria-label="Business card, front">
    <svg class="front-wave" viewBox="0 0 560 320" preserveAspectRatio="none" aria-hidden="true">
      <path d="M0 120 C 120 150, 200 175, 300 160 S 470 110, 560 135 L560 320 L0 320 Z" fill="var(--navy)"/>
      <path d="M0 138 C 120 168, 200 190, 300 176 S 470 128, 560 152" fill="none" stroke="var(--tan)" stroke-width="3"/>
    </svg>

    <div class="front-brand">
      <span class="brand-dot"></span>
      <span class="brand-name">Marlow Ridge<small>Veterinary Hospital</small></span>
    </div>

    <div class="details">
      <p class="holder-name">Glen H. Barrett, DVM, DABVP</p>
      <p class="holder-title">Board Certified Canine and Feline Practice</p>
      <div class="detail-cols">
        <address class="address">5720 FM 916<br>Alder Bend, TX 75190</address>
        <ul class="contacts">
          <li>
            <svg viewBox="0 0 10 10"><circle cx="5" cy="5" r="5" fill="var(--tan-light)"/><path d="M3.2 2.6l1 1-.5.7c.4.8 1 1.4 1.8 1.8l.7-.5 1 1-.6.8C4.8 7.3 2.7 5.2 2.6 3.2z" fill="var(--navy)"/></svg>
            214-555-0142
          </li>
          <li>
            <svg viewBox="0 0 10 10"><circle cx="5" cy="5" r="5" fill="var(--tan-light)"/><rect x="2.5" y="3.3" width="5" height="3.4" fill="none" stroke="var(--navy)" stroke-width="0.7"/><path d="M2.5 3.3L5 5.3 7.5 3.3" fill="none" stroke="var(--navy)" stroke-width="0.7"/></svg>
            <span class="email">mrvhvet@fenmail.example</span>
          </li>
          <li>
            <svg viewBox="0 0 10 10"><circle cx="5" cy="5" r="5" fill="var(--tan-light)"/><circle cx="5" cy="5" r="2.6" fill="none" stroke="var(--navy)" stroke-width="0.6"/><path d="M2.4 5h5.2M5 2.4c-1.2 1.4-1.2 3.8 0 5.2M5 2.4c1.2 1.4 1.2 3.8 0 5.2" fill="none" stroke="var(--navy)" stroke-width="0.5"/></svg>
            www.marlowridgevet.example
          </li>
        </ul>
      </div>
    </div>
  </section>

</body>
</html>
```